Business card for a gourmet fruit and vegetable retail store

Please design a business card for our boutique gourmet fruit and vegetable food store using attached logo design, with the colour options of white, black and lime green. We would like it to be unique and classic, with a large image of the logo on the back of the business card, and the business card details plus a design on the front.

Target Market(s)

High income earners in an affluent Melbourne suburb who value high quality products and done mind paying for it

Industry/Entity Type

Retail

Contact Information for Business Card

Business name: Harwick's Fine Food Merchant
Address: 27 Plumtree Rd, Kelsby VIC 3158
Name: TBC
Position Title: Director
Phone Number: TBC
Mobile: TBC

Business name is: Harwick's Fine Food Merchant. Please allow space for us to fill in the business address, contact number, person's name, position Title and mobile number.

Colors
acd036

Requirements
Must have
• The logo must have our business logo on the back, and our business details and contact details on the front. It must include the colours of white, black and lime green
Nice to have
• It can have different background colours on the front and on the back.
Should not have
• It should not have any other colours aside from white, black and lime green

```html
<!DOCTYPE html>
<html lang="en">
<head>
<meta charset="utf-8">
<title>Harwick's Fine Food Merchant – Business Card</title>
<link href="https://fonts.googleapis.com/css2?family=Oswald:wght@500&family=Open+Sans:wght@400;600&display=swap" rel="stylesheet">
<style>
  :root {
    --lime: #acd036;
    --ink: #1b1b1b;
    --white: #ffffff;
    --backdrop: #ecebe7;
  }
  * { margin: 0; padding: 0; box-sizing: border-box; }
  html, body {
    width: 1200px; height: 1000px; overflow: hidden;
    background: var(--backdrop);
    font-family: "Open Sans", Arial, sans-serif;
  }
  .card {
    position: absolute;
    left: 266px;
    width: 666px; height: 397px;
    border-radius: 22px;
    box-shadow: 0 6px 16px rgba(0,0,0,0.18);
  }
  .card--logo { top: 74px; background: var(--lime); }
  .card--details { top: 533px; background: var(--ink); color: var(--white); }

  .brand-mark {
    position: absolute; left: 194px; top: 61px;
    width: 274px; height: 274px;
    border: 2px solid var(--white); border-radius: 50%;
    display: flex; align-items: center; justify-content: center;
  }
  .brand-name {
    color: var(--white);
    font-family: "Open Sans", Arial, sans-serif;
    font-weight: 600; font-size: 34px; letter-spacing: 2px;
  }

  .identity {
    position: absolute; right: 372px; top: 170px;
    text-align: right;
  }
  .identity__name {
    font-family: "Oswald", "Arial Narrow", sans-serif;
    font-weight: 500; font-size: 25px; line-height: 30px;
    color: var(--lime); letter-spacing: 0.3px;
  }
  .identity__role { font-size: 15px; line-height: 20px; }

  .divider {
    position: absolute; left: 318px; top: 169px;
    width: 2px; height: 57px; background: var(--white);
  }

  .contacts {
    position: absolute; left: 345px; top: 165px;
    list-style: none; font-size: 15.5px; line-height: 22.5px;
  }
  .contacts li { display: flex; align-items: center; }
  .contacts svg { width: 14px; height: 14px; margin-right: 7px; fill: var(--lime); }

  .address {
    position: absolute; left: 0; right: 0; top: 348px;
    text-align: center; font-size: 16px;
  }
  .address__business { color: var(--lime); font-weight: 600; }
</style>
</head>
<body>
  <section class="card card--logo">
    <div class="brand-mark">
      <span class="brand-name">HARWICK'S</span>
    </div>
  </section>

  <section class="card card--details">
    <div class="identity">
      <div class="identity__name">LENA R. MARCHETTI</div>
      <div class="identity__role">Chief Executive Officer</div>
    </div>
    <div class="divider"></div>
    <ul class="contacts">
      <li>
        <svg viewBox="0 0 16 16" aria-hidden="true"><path d="M2 5c0-2 2-3 6-3s6 1 6 3v1h-3V5H5v1H2zM4 7h8l2 6H2z"/></svg>
        00 000 000 000
      </li>
      <li>
        <svg viewBox="0 0 16 16" aria-hidden="true"><path d="M5 1h6a1 1 0 0 1 1 1v12a1 1 0 0 1-1 1H5a1 1 0 0 1-1-1V2a1 1 0 0 1 1-1zm0 2v9h6V3zm3 10a.8.8 0 1 0 0 1.6A.8.8 0 0 0 8 13z"/></svg>
        00 000 000 000
      </li>
      <li>
        <svg viewBox="0 0 16 16" aria-hidden="true"><path d="M1 3h14v10H1zm1.5 1.5L8 9l5.5-4.5z"/></svg>
        info@harwickfinefood.com
      </li>
    </ul>
    <p class="address">
      <span class="address__business">Harwick's Fine Food Merchant</span> 27 Plumtree Rd, Kelsby VIC 3158
    </p>
  </section>
</body>
</html>
```